TV+Music+Social Network+Entertainment+brightlistin= Designers lol

TV+ Music+ Social Network +Entertainment+ brightlistin=

ZELLOPAK.COM

Zellopak is a one-stop shop promotional plateform that will communicate information to all user of what is COOL, NEW and Exicting in your Neighborhood.(News,Events,Entertainment,ect) We promote for all User/Entrepreneur/business/Talents.We are the future and dream destination for all to whom owns a computer. Forming the the World Wide Web into your Local Wide Web. (Atlanta, Dallas, Las Vegas, New York ect.)

* EX: ( WWW. ??? .com =LWW. ??? .com)
WORLD = LOCAL

* Goal/Mission: Have customer/user visit the website and then leave their house to go experience life in their respective surroundings.

/////////////////////////Web page///////////////////////

Colors:Blue/Green/black

include: interchangable background picture @ top (to update easily and keep fresh) On this background picture include logo (top left) login/sign (top left)

Major Tabs: Music/Daylife/Nightlife/Video/Shop

Industry/Entity Type

House

Requirements
Nice to have
• Tv screen/search engine

```html
<!DOCTYPE html>
<html lang="en">
<head>
<meta charset="utf-8">
<title>Zellopak – Your Local Wide Web</title>
<link href="https://fonts.googleapis.com/css2?family=Arimo:wght@400;700&family=PT+Serif:wght@400;700&display=swap" rel="stylesheet">
<style>
:root{
  --navy:#0b2a52;
  --navy-deep:#071d3b;
  --blue:#1b5da6;
  --blue-bright:#2f86d6;
  --green:#5aa526;
  --green-dark:#3f8116;
  --grey:#e6e7ea;
  --grey-line:#cfd2d7;
  --text:#444a52;
  --muted:#7a8088;
  --white:#fff;
}
*{box-sizing:border-box;margin:0;padding:0}
html,body{width:738px;height:1200px;overflow:hidden}
body{position:relative;font-family:"Arimo",Arial,sans-serif;font-size:8px;color:var(--text);background:var(--white)}
.serif{font-family:"PT Serif",Georgia,serif}

/* hero */
.hero{position:absolute;left:0;top:0;width:738px;height:372px;
  background:linear-gradient(180deg,#5f9fd0 0%,#8ec3e6 32%,#bfe0ee 48%,#43b6c8 56%,#6fcfd3 64%,#e9ddc0 76%,#d8c7a2 100%)}
.login{position:absolute;top:0;right:10px;display:flex;align-items:center;height:24px;gap:8px;background:rgba(7,29,59,.85);padding:0 8px 0 0;border-radius:0 0 4px 4px}
.login-tab{background:var(--green);color:#fff;font-weight:700;font-size:9px;height:24px;line-height:24px;padding:0 14px}
.login label{color:#fff;font-size:8px}
.login input{width:70px;height:13px;border:0;border-radius:2px}
.login-go{width:14px;height:14px;border-radius:3px;background:var(--blue-bright)}
.brand{position:absolute;left:86px;top:152px;display:flex;align-items:center;gap:6px}
.brand-dot{width:22px;height:22px;border-radius:50%;background:var(--blue-bright)}
.brand-name{font-size:22px;font-weight:700;color:#fff}

/* nav */
.nav{position:absolute;left:86px;top:182px;width:566px;height:24px;background:var(--navy);display:flex;align-items:center;padding-left:6px}
.search-box{display:flex;align-items:center;background:#fff;height:16px;width:150px;border-radius:2px;padding-left:5px;font-size:8px;color:var(--muted)}
.city{margin-left:3px;background:var(--blue);color:#fff;font-size:7px;font-weight:700;height:16px;line-height:16px;padding:0 8px;border-radius:2px}
.search-btn{margin-left:3px;background:var(--blue-bright);color:#fff;font-size:7px;font-weight:700;height:16px;line-height:16px;padding:0 8px;border-radius:2px}
.tabs{display:flex;margin-left:10px;height:24px}
.tabs a{color:#fff;text-decoration:none;font-weight:700;font-size:10px;padding:0 14px;line-height:24px;border-left:1px solid #1e4477}

/* slider */
.slider{position:absolute;left:86px;top:207px;width:566px;height:154px;background:#fff;border:2px solid var(--blue)}
.slide-photo{position:absolute;left:22px;top:14px;width:170px;height:96px;background:linear-gradient(135deg,#dfe6ee,#9fb0c4 60%,#556a84)}
.slide-copy{position:absolute;left:215px;top:14px;width:320px}
.slide-copy h2{font-size:16px;font-weight:700;color:var(--navy)}
.slide-copy p{margin-top:5px;font-size:7.5px;line-height:1.35;color:var(--muted)}
.slide-copy h4{margin-top:8px;font-size:8px;color:var(--blue)}
.slide-copy ul{list-style:none;font-size:7.5px;color:var(--muted);margin-top:2px}
.btn-green{display:inline-block;background:var(--green);color:#fff;font-size:7px;font-weight:700;padding:3px 9px;border-radius:2px}
.slide-copy .btn-green{margin-top:6px}
.arrow{position:absolute;top:52px;width:6px;height:14px;background:var(--blue)}
.arrow.l{left:-2px}.arrow.r{right:-2px}
.stats{position:absolute;right:0;bottom:0;width:380px;height:34px;background:var(--blue);display:flex;color:#fff}
.stat{padding:5px 10px;border-right:1px solid #3b79bd}
.stat b{display:block;font-size:13px}
.stat span{font-size:6.5px}
.stat.wide b{color:#b8e58a}

/* welcome */
.welcome{position:absolute;left:86px;top:372px;width:566px;height:226px}
.welcome-main{position:absolute;left:0;top:16px;width:345px}
.welcome-main h1{font-size:18px;color:var(--blue);font-weight:700}
.welcome-main p{margin-top:8px;font-size:7.5px;line-height:1.45;color:var(--muted)}
.today{position:absolute;left:372px;top:18px;width:194px}
.today h3{font-size:9px;color:var(--navy);font-weight:700}
.today-item{display:flex;gap:6px;margin-top:6px}
.today-thumb{width:38px;height:32px;background:linear-gradient(135deg,#6f7f95,#283a55)}
.today-item p{font-size:7px;color:var(--muted);line-height:1.3}
.today-item p b{color:var(--blue)}
.today ul{list-style:none;margin-top:6px}
.today li{font-size:7px;color:var(--muted);padding:2px 0;border-bottom:1px dotted var(--grey-line)}

/* columns */
.columns{position:absolute;left:0;top:598px;width:738px;height:368px;background:var(--grey)}
.col{position:absolute;top:12px;width:180px}
.col h2{font-size:12px;color:var(--navy);font-weight:700;padding-bottom:6px}
.card{background:#fff;border:1px solid var(--grey-line);height:324px;padding:8px}
.card h3{font-size:11px;font-weight:700;color:var(--navy);text-align:center;line-height:1.2}
.card-img{margin-top:6px;height:70px}
.card .caption{font-size:6px;color:var(--muted);text-align:center;margin-top:3px}
.card p{font-size:7px;line-height:1.35;color:var(--muted);margin-top:5px}
.card .more{text-align:right;margin-top:4px}
.card h4{font-size:7.5px;color:var(--navy);margin-top:8px}
.card ul{list-style:none;margin-top:3px}
.card li{font-size:6.5px;color:var(--muted);padding:2px 0 2px 8px;position:relative}
.card li::before{content:"";position:absolute;left:1px;top:5px;width:3px;height:3px;background:var(--blue)}
.media{display:flex;gap:5px;margin-top:4px;align-items:center}
.media i{width:26px;height:18px;background:linear-gradient(135deg,#5d6f88,#22344e);flex:none}
.media span{font-size:6.5px;color:var(--muted)}

/* footer */
.footer{position:absolute;left:0;top:966px;width:738px;height:234px;background:var(--navy)}
.newsletter{position:absolute;left:86px;top:16px;display:flex;align-items:center;gap:6px;color:#fff;font-size:10px}
.newsletter input{width:110px;height:16px;border:0;border-radius:2px}
.newsletter .sub{background:var(--green);font-size:8px;font-weight:700;padding:4px 10px;border-radius:2px}
.quote{position:absolute;left:470px;top:12px;display:flex;gap:6px;align-items:center;color:#fff}
.quote-ico{width:22px;height:22px;border-radius:50%;background:var(--blue-bright)}
.quote b{display:block;font-size:9px}
.quote span{font-size:10px;color:#b8e58a;font-weight:700}
.foot-nav{position:absolute;left:86px;top:62px;display:flex;gap:14px}
.foot-link{width:34px;text-align:center;color:#cfe0f4;font-size:7px}
.foot-link svg{display:block;margin:0 auto 3px}
.foot-extra{position:absolute;left:380px;top:62px;display:flex;gap:16px}
.extra{color:#fff;font-size:8px;display:flex;gap:4px}
.extra small{display:block;font-size:6px;color:#8fa6c4}
.extra i{width:14px;height:14px;border-radius:3px;background:var(--blue-bright);flex:none}
.foot-row{position:absolute;left:140px;top:110px;display:flex;gap:26px;align-items:center;color:#fff}
.pill{background:var(--blue);padding:6px 12px;border-radius:3px;font-weight:700;font-size:9px}
.pill.green{background:var(--green-dark)}
.follow{display:flex;gap:4px;align-items:center;font-size:7px}
.follow i{width:14px;height:14px;border-radius:2px;background:#2a5f9e}
.follow i:nth-child(3){background:#3a7bc4}.follow i:nth-child(4){background:#b93434}
.legal{position:absolute;left:0;bottom:0;width:738px;height:28px;background:var(--navy-deep);display:flex;justify-content:center;align-items:center;gap:14px;color:#8fa6c4;font-size:6.5px}
</style>
</head>
<body>

<header class="hero" role="img" aria-label="Tropical beach with thatched umbrellas, white sand and turquoise sea">
  <form class="login">
    <span class="login-tab">LOGIN IN</span>
    <label>Username</label><input type="text" aria-label="Username">
    <label>Password</label><input type="password" aria-label="Password">
    <span class="login-go"></span>
  </form>
  <div class="brand"><span class="brand-dot"></span><span class="brand-name">Zellopak</span></div>
</header>

<nav class="nav">
  <div class="search-box">I am looking for</div>
  <span class="city">ATLANTA ▾</span>
  <span class="search-btn">SEARCH</span>
  <div class="tabs"><a>MUSIC</a><a>DAYLIFE</a><a>NIGHTLIFE</a><a>VIDEO</a><a>SHOP</a></div>
</nav>

<section class="slider">
  <span class="arrow l"></span><span class="arrow r"></span>
  <div class="slide-photo" role="img" aria-label="Rock band performing on stage with guitars"></div>
  <div class="slide-copy">
    <h2 class="serif">Music Event Organisers</h2>
    <p>Local bands, venues and promoters in one place. Find the next live show near you and book your tickets before they sell out.</p>
    <h4>Service Types</h4>
    <ul><li>› Concert Hire | Stage Setup</li></ul>
    <span class="btn-green">READ MORE</span>
  </div>
  <div class="stats">
    <div class="stat"><b>25+ YEARS OF EXPERIENCE</b><span>IN CONNECTING CUSTOMERS TO SUPPLIERS</span></div>
    <div class="stat wide"><b>250+</b><span>CUSTOMERS</span></div>
    <div class="stat wide"><b>50,000+</b><span>SUPPLIERS</span></div>
  </div>
</section>

<section class="welcome">
  <div class="welcome-main">
    <h1 class="serif">Welcome to Zellopak</h1>
    <p>Zellopak turns the world wide web into your local wide web. Discover what is cool, new and exciting in your neighborhood, from live music and daytime events to nightlife, video and shopping. We promote users, entrepreneurs, businesses and talents so the whole city can find them.</p>
    <p>Browse your city, pick a plan and then step out the door to experience life in your own surroundings. Every week brings fresh news, new venues and new faces to follow.</p>
  </div>
  <aside class="today">
    <h3>Today on Zellopak News</h3>
    <div class="today-item">
      <div class="today-thumb" role="img" aria-label="Portrait thumbnail for news story"></div>
      <p><b>Fall Classic Week</b><br>Block party lineup announced for downtown this Friday.</p>
    </div>
    <ul>
      <li>· New rooftop bar opens on main street</li>
      <li>· Free jazz in the park on sunday</li>
      <li>· Weekend farmers market returns</li>
    </ul>
  </aside>
</section>

<section class="columns">
  <div class="col" style="left:86px">
    <h2 class="serif">Latest News</h2>
    <article class="card">
      <h3 class="serif">City lights up for summer festival</h3>
      <div class="card-img" role="img" aria-label="Crowd at an evening festival stage" style="background:linear-gradient(135deg,#1d3c6e,#c2563a)"></div>
      <div class="caption">Festival crowd downtown</div>
      <p>Thousands gathered downtown for the opening night of the summer festival with music, food and art.</p>
      <div class="more"><span class="btn-green">MORE</span></div>
      <h4>More Headlines</h4>
      <ul><li>New venue opens near the river</li><li>Local talent signs record deal</li><li>Food trucks return this weekend</li><li>Street art tour starts in June</li><li>Parks host free movie nights</li></ul>
    </article>
  </div>
  <div class="col" style="left:279px">
    <h2 class="serif">Events</h2>
    <article class="card">
      <h3 class="serif">Open air concert in the park</h3>
      <div class="card-img" role="img" aria-label="Performer on stage under bright lights" style="background:linear-gradient(135deg,#2a7fd0,#e3b341)"></div>
      <div class="caption">Live stage this saturday</div>
      <p>Bring a blanket and friends for an evening of live bands under the stars in the city park.</p>
      <div class="more"><span class="btn-green">MORE</span></div>
      <h4>More Events</h4>
      <ul><li>Comedy night at the lounge</li><li>Art walk on first friday</li><li>Charity run around the lake</li><li>Salsa class for beginners</li><li>Wine tasting at the pier</li></ul>
    </article>
  </div>
  <div class="col" style="left:472px">
    <h2 class="serif">Entertainment</h2>
    <article class="card">
      <h3 class="serif">New film tour stops in town</h3>
      <div class="card-img" role="img" aria-label="Film premiere scene with blue lighting" style="background:linear-gradient(135deg,#0f2d5c,#4f8fd6)"></div>
      <div class="caption">Premiere night</div>
      <p>The touring film series screens at the grand theater with a live talk afterward.</p>
      <div class="more"><span class="btn-green">MORE</span></div>
      <h4>More</h4>
      <div class="media"><i role="img" aria-label="Video thumbnail"></i><span>Top ten shows this month</span></div>
      <div class="media"><i role="img" aria-label="Video thumbnail"></i><span>Backstage with the crew</span></div>
      <div class="media"><i role="img" aria-label="Video thumbnail"></i><span>Weekend playlist picks</span></div>
    </article>
  </div>
</section>

<footer class="footer">
  <div class="newsletter">Newsletter <input type="text" aria-label="Email"> <span class="sub">Subscribe</span></div>
  <div class="quote"><span class="quote-ico"></span><div><b>QUERIES OR FREE QUOTES</b><span>CALL 1-800-555-0142</span></div></div>
  <div class="foot-nav">
    <div class="foot-link"><svg width="20" height="18" viewBox="0 0 20 18"><path d="M2 9 10 2l8 7v8H2z" fill="#4d8fd6"/></svg>House</div>
    <div class="foot-link"><svg width="20" height="18" viewBox="0 0 20 18"><circle cx="10" cy="9" r="6" fill="#e3b341"/></svg>Daylife</div>
    <div class="foot-link"><svg width="20" height="18" viewBox="0 0 20 18"><path d="M12 2a7 7 0 1 0 6 10 6 6 0 0 1-6-10z" fill="#9fb8e0"/></svg>Nightlife</div>
    <div class="foot-link"><svg width="20" height="18" viewBox="0 0 20 18"><rect x="2" y="4" width="16" height="11" rx="2" fill="#4d8fd6"/><path d="M8 7v5l5-2.5z" fill="#fff"/></svg>Video</div>
    <div class="foot-link"><svg width="20" height="18" viewBox="0 0 20 18"><path d="M4 6h12l-1 10H5z" fill="#5aa526"/></svg>Shop</div>
  </div>
  <div class="foot-extra">
    <div class="extra"><i></i><div>Blog<small>latest posts</small></div></div>
    <div class="extra"><i></i><div>News<small>city updates</small></div></div>
    <div class="extra"><i></i><div>Events<small>this week</small></div></div>
  </div>
  <div class="foot-row">
    <span class="pill">TESTIMONIALS</span>
    <span class="pill green">ADVERTISE WITH US</span>
    <span class="pill">SEND US YOUR FEEDBACK</span>
    <span class="follow">Follow us <i></i><i></i><i></i><i></i></span>
  </div>
  <div class="legal"><span>Advertise with Zellopak</span><span>About Us</span><span>Contact Us</span><span>Privacy Policy</span><span>Terms of Service</span><span>© 2012 Zellopak</span></div>
</footer>

</body>
</html>
```